Business Card Design for a Software Startup

We'd like to have a business card design. We already have a logo. Basically what we need is a clean design with name, address, cellphone and phone numbers, e-mail and web site address (front) and a space on the back with our logo with the company name on the right side and some texts on the bottom.
We are a development and consulting company in Brazil with highly qualified team of professionals in Java, iOS and Android development and consulting.

Target Market(s)

CIO, IT managers of mid to big size companies

Industry/Entity Type

Business

```html
<!DOCTYPE html>
<html lang="en">
<head>
<meta charset="utf-8">
<title>VELORA Business Cards</title>
<link rel="stylesheet" href="https://fonts.googleapis.com/css2?family=Arimo:wght@400;700&display=swap">
<style>
  :root {
    --navy: #14497a;
    --navy-deep: #0d3a66;
    --blue: #1f6fb0;
    --sky: #2a9ad6;
    --label: #2f8fcf;
    --ink: #3d4650;
    --rule: #c9ced4;
    --paper: #ffffff;
    --backdrop: #eceef1;
  }
  * { margin: 0; padding: 0; box-sizing: border-box; }
  html, body {
    width: 1200px;
    height: 720px;
    overflow: hidden;
    background: var(--backdrop);
    font-family: "Arimo", Arial, sans-serif;
  }
  .canvas {
    position: relative;
    width: 1200px;
    height: 720px;
  }
  .card {
    position: absolute;
    top: 205px;
    width: 540px;
    height: 310px;
    overflow: hidden;
    box-shadow: 0 6px 18px rgba(0, 0, 0, 0.18);
  }

  /* Front */
  .card-front { left: 40px; background: var(--paper); }
  .front-waves { position: absolute; left: 0; top: 0; width: 540px; height: 310px; }
  .brand {
    position: absolute;
    left: 40px;
    top: 60px;
    width: 170px;
    display: flex;
    flex-direction: column;
    align-items: center;
    gap: 12px;
  }
  .brand-square {
    width: 96px;
    height: 96px;
    border-radius: 12px;
    background: var(--blue);
  }
  .brand-name {
    font-size: 34px;
    font-weight: 700;
    color: var(--navy-deep);
    letter-spacing: 1px;
  }
  .divider {
    position: absolute;
    left: 232px;
    top: 34px;
    width: 1px;
    height: 160px;
    background: var(--rule);
  }
  .contact {
    position: absolute;
    left: 248px;
    top: 34px;
    color: var(--ink);
  }
  .contact-name { font-size: 19px; font-weight: 700; color: var(--navy); }
  .contact-title { font-size: 13px; margin-bottom: 8px; }
  .contact-line { font-size: 13px; line-height: 19px; }
  .contact-line .label { color: var(--label); display: inline-block; width: 20px; }
  .contact-address { font-size: 12px; line-height: 16px; margin-top: 8px; }
  .front-web {
    position: absolute;
    right: 28px;
    bottom: 62px;
    color: var(--paper);
    font-size: 13px;
    letter-spacing: 2px;
  }

  /* Back */
  .card-back {
    left: 620px;
    background: linear-gradient(135deg, var(--navy) 0%, var(--navy-deep) 100%);
    color: var(--paper);
  }
  .back-name {
    position: absolute;
    left: 0;
    right: 0;
    top: 100px;
    text-align: center;
    font-size: 72px;
    font-weight: 700;
    letter-spacing: 2px;
  }
  .back-domain {
    position: absolute;
    right: 80px;
    top: 186px;
    font-size: 16px;
    letter-spacing: 1px;
  }
  .back-web {
    position: absolute;
    left: 0;
    right: 0;
    bottom: 34px;
    text-align: center;
    font-size: 17px;
    font-weight: 700;
    letter-spacing: 4px;
  }
</style>
</head>
<body>
<main class="canvas">

  <section class="card card-front" aria-label="Card front">
    <svg class="front-waves" viewBox="0 0 540 310" aria-hidden="true">
      <path d="M0 268 C140 300 300 200 540 178 L540 190 C310 212 150 310 0 282 Z" fill="var(--sky)"/>
      <path d="M0 300 C180 300 300 218 540 196 L540 310 L0 310 Z" fill="var(--navy)"/>
      <path d="M0 250 C150 290 300 190 540 160" fill="none" stroke="var(--navy)" stroke-width="1.5"/>
    </svg>
    <div class="brand">
      <div class="brand-square"></div>
      <div class="brand-name">VELORA</div>
    </div>
    <div class="divider"></div>
    <div class="contact">
      <div class="contact-name">Your Name</div>
      <div class="contact-title">Title</div>
      <div class="contact-line"><span class="label">P:</span>123-456-7890</div>
      <div class="contact-line"><span class="label">C:</span>123-456-7890</div>
      <div class="contact-line"><span class="label">E:</span>yourname@velora.com</div>
      <div class="contact-address">Door No. Street Name<br>City Name, State, Zip Code</div>
    </div>
    <div class="front-web">www.velora.com</div>
  </section>

  <section class="card card-back" aria-label="Card back">
    <div class="back-name">VELORA</div>
    <div class="back-domain">velora.com</div>
    <div class="back-web">www.velora.com</div>
  </section>

</main>
</body>
</html>
```